Flyer Tally Desk Ledger Kit

Hi
Can you please design me a DL Flyer for: Tally Desk Ledger Kit
Info:
Starting a new Business ?
Want to save on bookkeeping fees for your existing business?

You can now save 1000's off bookkeeping fees by Doing it Yourself.

Using our Bookkeeper software you simply key in the information as you go.

We offer one on one training, backup and support.
We can assist you with BAS Preparation and Payrol Advice.

Add Modules as required:
Point of Sale Module
Jobs Management Module
Website Intergration Module

Fee set up assistance and training.

Lets get the ball rolling: 1300 462 815
www.tldlk.com.au
admin@tldlk.com.au (use the logo thing you made)

Target Market(s)

Small Business

Colors
ec1f27
f04a50
f59296
fcdcdc
ffffff

Requirements
Nice to have
• image/s related to bookkeeping

```html
<!DOCTYPE html>
<html lang="en">
<head>
<meta charset="utf-8">
<title>Tally Desk Ledger Kit – DL Flyer</title>
<link rel="stylesheet" href="https://fonts.googleapis.com/css2?family=Open+Sans:wght@400;600;700&family=Roboto+Condensed:wght@400;700&display=swap">
<style>
  :root {
    --red: #ec1f27;
    --red-soft: #f04a50;
    --pink: #f59296;
    --blush: #fcdcdc;
    --white: #ffffff;
    --charcoal: #3a3a3c;
    --slate: #5a5a5d;
    --ink: #58595b;
    --stage: #e9e9eb;
  }
  * { box-sizing: border-box; margin: 0; padding: 0; }
  html, body { width: 780px; height: 1200px; overflow: hidden; }
  body { background: var(--stage); font-family: "Open Sans", sans-serif; }

  .flyer {
    position: absolute; left: 112px; top: 20px;
    width: 556px; height: 1160px;
    background: var(--white);
    overflow: hidden;
    box-shadow: 0 2px 10px rgba(0,0,0,.18);
  }

  /* Header / brand */
  .brand {
    position: absolute; left: 0; top: 0; width: 100%; height: 160px;
    display: flex; align-items: center; justify-content: center;
    padding-bottom: 20px;
  }
  .brand-row { display: flex; align-items: center; gap: 12px; }
  .brand-dot { width: 34px; height: 34px; border-radius: 50%; background: var(--red); }
  .brand-name {
    font-family: "Roboto Condensed", sans-serif; font-weight: 700;
    font-size: 40px; color: var(--red); letter-spacing: .2px;
  }

  /* Photo band */
  .photo {
    position: absolute; left: 0; top: 150px; width: 100%; height: 440px;
    background:
      radial-gradient(ellipse at 55% 45%, #f4f3f1 0%, #e3e1de 45%, #b9b7b5 80%, #8f8e8d 100%);
  }
  .photo-curve { position: absolute; left: 0; top: 140px; width: 100%; height: 80px; }

  /* Dark info panel */
  .panel {
    position: absolute; left: 0; top: 545px; width: 100%; height: 490px;
    background: radial-gradient(ellipse at 50% 10%, var(--slate) 0%, var(--charcoal) 75%);
  }
  .panel-curve { position: absolute; left: 0; top: 520px; width: 100%; height: 60px; }

  .headline {
    position: absolute; left: 30px; top: 588px; width: 496px;
    font-family: "Roboto Condensed", sans-serif; font-weight: 700;
    font-size: 35px; color: var(--white); letter-spacing: .3px; white-space: nowrap;
  }
  .headline em { font-style: normal; color: var(--red); }
  .headline-rule {
    position: absolute; left: 30px; top: 641px; width: 496px; height: 3px; background: var(--red);
  }
  .subhead {
    position: absolute; left: 30px; top: 657px; width: 496px;
    font-size: 15.5px; color: var(--white); white-space: nowrap;
  }
  .offer {
    position: absolute; left: 24px; top: 699px; width: 508px; height: 78px;
    background: var(--red); border: 2px solid var(--red-soft);
    box-shadow: 0 3px 6px rgba(0,0,0,.35);
    display: flex; align-items: center; justify-content: center; text-align: center;
    font-family: "Open Sans", sans-serif; font-weight: 700; font-size: 18.5px;
    line-height: 1.3; color: var(--white); text-transform: uppercase;
  }

  .services { position: absolute; left: 34px; top: 797px; list-style: none; }
  .services li {
    display: flex; align-items: center; gap: 10px;
    font-size: 15.5px; color: var(--white); height: 25px;
  }
  .tick { width: 15px; height: 15px; flex: none; }

  .modules-title {
    position: absolute; left: 34px; top: 866px;
    font-family: "Roboto Condensed", sans-serif; font-weight: 700; font-size: 17px;
    color: var(--red); text-decoration: underline; text-underline-offset: 3px; text-transform: uppercase;
  }
  .modules { position: absolute; left: 26px; top: 900px; list-style: none; }
  .modules li {
    display: flex; align-items: center; gap: 10px;
    font-size: 16px; color: var(--white); height: 39px;
  }
  .module-icon { width: 28px; height: 28px; flex: none; }

  .callout-glow {
    position: absolute; left: 410px; top: 846px; width: 130px; height: 130px;
    border-radius: 50%; background: var(--pink); opacity: .45;
  }
  .callout {
    position: absolute; left: 372px; top: 862px; width: 158px; height: 158px;
    border-radius: 50%; background: var(--red);
    display: flex; align-items: center; justify-content: center; text-align: center;
    font-size: 12.5px; line-height: 1.4; color: var(--white); padding: 0 18px;
  }

  /* Contact band */
  .cta {
    position: absolute; left: 0; top: 1032px; width: 100%; height: 64px;
    background: var(--red);
    display: flex; align-items: center; justify-content: center; gap: 8px;
    font-family: "Open Sans", sans-serif; font-weight: 700; font-size: 22px; color: var(--white);
  }
  .cta-phone-icon { width: 24px; height: 30px; }

  .web {
    position: absolute; left: 0; top: 1096px; width: 100%; height: 64px;
    display: flex; align-items: center; justify-content: center;
    font-family: "Open Sans", sans-serif; font-weight: 700; font-size: 26px; color: var(--ink);
  }
</style>
</head>
<body>
<article class="flyer">

  <header class="brand">
    <div class="brand-row">
      <span class="brand-dot"></span>
      <span class="brand-name">Tally Desk Ledger Kit</span>
    </div>
  </header>

  <div class="photo" role="img" aria-label="Photo: hands working on a laptop on a white desk with a cup of coffee, phone and glasses"></div>

  <svg class="photo-curve" viewBox="0 0 556 80" preserveAspectRatio="none" aria-hidden="true">
    <path d="M0 0 H556 V22 Q300 8 0 70 Z" fill="#ffffff"/>
    <path d="M0 70 Q300 8 556 22 V30 Q300 18 0 78 Z" fill="#8c8c8e" opacity=".7"/>
  </svg>

  <div class="panel"></div>
  <svg class="panel-curve" viewBox="0 0 556 60" preserveAspectRatio="none" aria-hidden="true">
    <path d="M0 60 V30 Q280 -5 556 22 V60 Z" fill="#4b4b4e"/>
    <path d="M0 30 Q280 -5 556 22 V27 Q280 2 0 36 Z" fill="#a3a3a5" opacity=".6"/>
  </svg>

  <h1 class="headline">STARTING A <em>NEW</em> BUSINESS?</h1>
  <div class="headline-rule"></div>
  <p class="subhead">Want to save on bookkeeping fees for your existing business?</p>

  <p class="offer">You can now save 1000's off bookkeeping<br>fees by doing it yourself!!!</p>

  <ul class="services">
    <li><svg class="tick" viewBox="0 0 16 16"><circle cx="8" cy="8" r="7" fill="none" stroke="#ec1f27" stroke-width="1.6"/><path d="M4.6 8.2 7 10.4 11.4 5.8" fill="none" stroke="#ec1f27" stroke-width="1.8"/></svg>We offer one on one training, backup and support.</li>
    <li><svg class="tick" viewBox="0 0 16 16"><circle cx="8" cy="8" r="7" fill="none" stroke="#ec1f27" stroke-width="1.6"/><path d="M4.6 8.2 7 10.4 11.4 5.8" fill="none" stroke="#ec1f27" stroke-width="1.8"/></svg>We can assist you with BAS Preparation and Payrol Advice.</li>
  </ul>

  <h2 class="modules-title">Add modules as required:</h2>
  <ul class="modules">
    <li>
      <svg class="module-icon" viewBox="0 0 28 28" fill="none" stroke="#b5b5b7" stroke-width="1.6">
        <rect x="4" y="16" width="4" height="9"/><rect x="11" y="12" width="4" height="13"/><rect x="18" y="8" width="4" height="17"/><path d="M3 12 10 6 15 9 24 3"/>
      </svg>Point of Sale Module</li>
    <li>
      <svg class="module-icon" viewBox="0 0 28 28" fill="none" stroke="#b5b5b7" stroke-width="1.6">
        <circle cx="10" cy="9" r="4"/><path d="M3 24c0-5 3-8 7-8s7 3 7 8"/><circle cx="20" cy="11" r="3"/><path d="M18 17c4 0 7 2 7 7"/>
      </svg>Jobs Management Module</li>
    <li>
      <svg class="module-icon" viewBox="0 0 28 28" fill="none" stroke="#b5b5b7" stroke-width="1.6">
        <rect x="3" y="4" width="22" height="15" rx="1"/><path d="M10 24h8M14 19v5"/><path d="M8 9h12M8 13h8"/>
      </svg>Website Intergration Module</li>
  </ul>

  <div class="callout-glow"></div>
  <p class="callout">Using our Bookkeeper software you SIMPLY KEY in the information as you go.</p>

  <footer>
    <div class="cta">
      <span>Lets get the ball rolling:</span>
      <svg class="cta-phone-icon" viewBox="0 0 24 30" aria-hidden="true">
        <rect x="5" y="2" width="14" height="26" rx="2.5" fill="none" stroke="#ffffff" stroke-width="2.4"/>
        <circle cx="12" cy="23.5" r="1.6" fill="#ffffff"/>
      </svg>
      <span>1300 462 815</span>
    </div>
    <div class="web">www.tldlk.com.au</div>
  </footer>

</article>
</body>
</html>
```